Business card and (possibly) logo

Hi - we need a new business card.
We have an existing logo that we quite like but we are open to options.
We are an architectural firm - we specialize in upmarket residential work and apartment blocks.
We are chasing a business card at present but also want to extensively update our website going forward to attract a much higher level of client / investor / developer.
Our current logo is black, grey and yellow and based on the sun/moon temples in Mexico.
We are open to variations.
We want to communicate professionalism, trust, quality.
Our website is www.korvalstudio.com.au - but note as above - we want to change the website as well to be a lot 'classier' and to appeal to a higher end market.

thanks

Target Market(s)

We are an architect firm - our target market is Developers and builders of high end houses and luxury apartment blocks. Also private home owners wanting to build excellent expensive houses. (ideally over $1m budgets)

Industry/Entity Type

Residential

Requirements
Must have
• Logo
Contact details;
Name
phone, mobile, email, web

```html
<!DOCTYPE html>
<html lang="en">
<head>
<meta charset="utf-8">
<title>Korval Studio – Business Card</title>
<link href="https://fonts.googleapis.com/css2?family=Cabin:wght@400;500;700&display=swap" rel="stylesheet">
<style>
  :root {
    --bg-light: #f1f1f1;
    --bg-dark: #bdbdbd;
    --card: #fbfbfa;
    --ink: #1a1a1a;
    --grey: #6f6f6f;
    --grey-soft: #9a9a9a;
    --accent: #f2a81d;
    --band: #141414;
    --faint: #ececec;
    --social: #5b88b8;
  }
  * { margin: 0; padding: 0; box-sizing: border-box; }
  html, body { width: 1200px; height: 787px; overflow: hidden; }
  body {
    background: radial-gradient(ellipse at 50% 40%, var(--bg-light) 0%, var(--bg-dark) 100%);
    font-family: "Cabin", Arial, sans-serif;
    position: relative;
  }
  .card {
    position: absolute;
    top: 235px;
    width: 520px;
    height: 317px;
    background: var(--card);
    box-shadow: 0 10px 24px rgba(0,0,0,.22);
    overflow: hidden;
  }
  .card-front { left: 55px; }
  .card-back { left: 625px; }
  .card-band {
    position: absolute; left: 0; right: 0; bottom: 0;
    height: 22px; background: var(--band);
  }
  .wordmark {
    position: absolute;
    display: flex; align-items: center; gap: 10px;
    font-weight: 700; color: var(--ink);
    letter-spacing: .02em; text-transform: uppercase;
    white-space: nowrap;
  }
  .wordmark-mark { background: var(--accent); flex: none; }
  .card-front .wordmark { left: 36px; top: 128px; font-size: 25px; }
  .card-front .wordmark-mark { width: 22px; height: 22px; }
  .call {
    position: absolute; left: 318px; top: 96px;
  }
  .call-label { font-size: 17px; color: var(--grey); }
  .call-number { font-size: 22px; font-weight: 700; color: var(--accent); letter-spacing: .03em; margin-top: 2px; white-space: nowrap; }
  .social {
    position: absolute; right: 34px; bottom: 44px; text-align: left;
  }
  .social-label { font-size: 12px; color: var(--grey); margin-bottom: 4px; }
  .social-list { display: flex; gap: 6px; }
  .social-list span {
    width: 26px; height: 26px; border-radius: 5px; background: var(--social);
  }
  .person { position: absolute; left: 40px; top: 38px; }
  .person-name { font-size: 15px; font-weight: 700; color: var(--accent); letter-spacing: .03em; }
  .person-role { font-size: 15px; color: var(--grey); margin-top: 2px; }
  .contacts { position: absolute; left: 190px; top: 36px; list-style: none; color: var(--grey); font-size: 14px; }
  .contacts li { display: flex; align-items: flex-start; line-height: 18px; }
  .contacts .gap { margin-top: 12px; }
  .contacts svg { width: 13px; height: 13px; margin-top: 2px; flex: none; }
  .contacts .sep { margin: 0 6px; color: var(--grey-soft); }
  .decor {
    position: absolute; left: -30px; bottom: 22px;
    width: 200px; height: 130px; background: var(--faint);
  }
  .card-back .wordmark { right: 40px; bottom: 56px; font-size: 24px; }
</style>
</head>
<body>
  <section class="card card-front">
    <div class="wordmark"><span class="wordmark-mark"></span>Korval Studio</div>
    <div class="call">
      <p class="call-label">Call us now on:</p>
      <p class="call-number">1300 72 18 45</p>
    </div>
    <div class="social">
      <p class="social-label">Find us on:</p>
      <div class="social-list"><span></span><span></span><span></span><span></span></div>
    </div>
    <div class="card-band"></div>
  </section>

  <section class="card card-back">
    <div class="decor" role="img" aria-label="Faint decorative brand shape"></div>
    <div class="person">
      <p class="person-name">FIRST NAME</p>
      <p class="person-role">Designation</p>
    </div>
    <ul class="contacts">
      <li><svg viewBox="0 0 16 16"><path d="M4 1h3l1 4-2 1a8 8 0 0 0 4 4l1-2 4 1v3c0 1-1 2-2 2A13 13 0 0 1 2 3c0-1 1-2 2-2z" fill="none" stroke="#888" stroke-width="1.3"/></svg><span class="sep">|</span>0412 555 018</li>
      <li><svg viewBox="0 0 16 16"><rect x="1" y="3" width="14" height="10" fill="none" stroke="#888" stroke-width="1.3"/><path d="M1 3l7 6 7-6" fill="none" stroke="#888" stroke-width="1.3"/></svg><span class="sep">|</span>firstname@korvalstudio.com.au</li>
      <li><svg viewBox="0 0 16 16"><circle cx="8" cy="8" r="6.5" fill="none" stroke="#888" stroke-width="1.3"/><path d="M1.5 8h13M8 1.5c-3 3.5-3 9.5 0 13M8 1.5c3 3.5 3 9.5 0 13" fill="none" stroke="#888" stroke-width="1"/></svg><span class="sep">|</span>www.korvalstudio.com.au</li>
      <li class="gap"><svg viewBox="0 0 16 16"><rect x="1" y="4" width="14" height="9" fill="none" stroke="#888" stroke-width="1.3"/><path d="M5 4V2h6v2" fill="none" stroke="#888" stroke-width="1.3"/></svg><span class="sep">|</span>1048 Westbrook WA 6911</li>
      <li class="gap"><svg viewBox="0 0 16 16"><rect x="3" y="1" width="10" height="14" fill="none" stroke="#888" stroke-width="1.3"/><path d="M6 4h1M9 4h1M6 7h1M9 7h1M6 10h1M9 10h1" stroke="#888" stroke-width="1.3"/></svg><span class="sep">|</span><span>Suite 8, 12 - 18 Harbourview<br>Parade, Westbrook, WA 6011</span></li>
    </ul>
    <div class="wordmark">Korval Studio</div>
    <div class="card-band"></div>
  </section>
</body>
</html>
```